Business Card Design for LeafSpire (Farming Devices)

We need Business Cards for our new Company based in Switzerland called "LeafSpire" We develop innovativ products for indoor and outdoor Farming for household and components for vertical farming. Our initial BloomNook gives people the possibility to grow their own food at home all year round. The design should communicate freshness, innovation, health.

```html
<!DOCTYPE html>
<html lang="en">
<head>
<meta charset="utf-8">
<title>LeafSpire – Business Card</title>
<link rel="stylesheet" href="https://fonts.googleapis.com/css2?family=Nunito+Sans:wght@700&family=Arimo:wght@400;700&display=swap">
<style>
  :root {
    --backdrop: #e9e9e9;
    --card-white: #ffffff;
    --brand-blue: #0a6fc2;
    --brand-green: #6cb33f;
    --text-gray: #555a5e;
    --card-shadow: 0 10px 24px rgba(0, 0, 0, 0.18);
  }
  * { margin: 0; padding: 0; box-sizing: border-box; }
  html, body {
    width: 1200px;
    height: 802px;
    overflow: hidden;
    background: var(--backdrop);
  }
  .canvas {
    position: relative;
    width: 1200px;
    height: 802px;
    display: flex;
    align-items: center;
    justify-content: center;
    gap: 40px;
  }
  .card {
    position: relative;
    width: 540px;
    height: 308px;
    box-shadow: var(--card-shadow);
    overflow: hidden;
  }
  .card--front { background: var(--card-white); }
  .card--back {
    background: var(--brand-blue);
    display: flex;
    align-items: center;
    justify-content: center;
  }
  .wordmark {
    font-family: "Nunito Sans", sans-serif;
    font-weight: 700;
    letter-spacing: 0.5px;
    line-height: 1;
  }
  .card--front .wordmark {
    position: absolute;
    left: 42px;
    top: 132px;
    font-size: 40px;
    color: var(--brand-green);
  }
  .card--back .wordmark {
    font-size: 52px;
    color: var(--card-white);
  }
  .contact {
    position: absolute;
    left: 300px;
    top: 104px;
    font-family: "Arimo", sans-serif;
    color: var(--text-gray);
  }
  .contact__name {
    font-weight: 700;
    font-size: 17px;
    letter-spacing: 0.4px;
    color: var(--brand-green);
    text-transform: uppercase;
  }
  .contact__role {
    font-size: 13px;
    margin: 3px 0 12px;
  }
  .contact__list { list-style: none; }
  .contact__item {
    display: flex;
    align-items: center;
    gap: 7px;
    font-size: 13.5px;
    margin-bottom: 5px;
  }
  .contact__icon {
    width: 12px;
    height: 12px;
    flex: none;
    fill: var(--brand-green);
  }
  .contact__accent { color: var(--brand-green); }
</style>
</head>
<body>
<main class="canvas">
  <section class="card card--front" aria-label="Business card front">
    <div class="wordmark">LeafSpire</div>
    <div class="contact">
      <p class="contact__name">Martin Keller</p>
      <p class="contact__role">Manager</p>
      <ul class="contact__list">
        <li class="contact__item">
          <svg class="contact__icon" viewBox="0 0 24 24" aria-hidden="true"><path d="M6.6 10.8a15.1 15.1 0 0 0 6.6 6.6l2.2-2.2a1 1 0 0 1 1-.25 11.4 11.4 0 0 0 3.6.57 1 1 0 0 1 1 1V20a1 1 0 0 1-1 1A17 17 0 0 1 3 4a1 1 0 0 1 1-1h3.5a1 1 0 0 1 1 1c0 1.25.2 2.45.57 3.57a1 1 0 0 1-.25 1z"/></svg>
          <span>041-555-0178</span>
        </li>
        <li class="contact__item">
          <svg class="contact__icon" viewBox="0 0 24 24" aria-hidden="true"><path d="M2 5h20v14H2z M4 7v.4l8 5 8-5V7l-8 5z" fill-rule="evenodd"/></svg>
          <span>hello@leafspire.ch</span>
        </li>
        <li class="contact__item">
          <svg class="contact__icon" viewBox="0 0 24 24" aria-hidden="true"><path d="M12 2a10 10 0 1 0 0 20 10 10 0 0 0 0-20zm6.9 6h-2.9a15.7 15.7 0 0 0-1.4-3.6A8 8 0 0 1 18.9 8zM12 4c.8 1.2 1.5 2.5 1.9 4h-3.8c.4-1.5 1.1-2.8 1.9-4zM4.3 14a8 8 0 0 1 0-4h3.4a16.5 16.5 0 0 0 0 4zm.8 2h2.9c.3 1.3.8 2.5 1.4 3.6A8 8 0 0 1 5.1 16zM8 8H5.1a8 8 0 0 1 4.3-3.6C8.8 5.5 8.3 6.7 8 8zm4 12c-.8-1.2-1.5-2.5-1.9-4h3.8c-.4 1.5-1.1 2.8-1.9 4zm2.3-6H9.7a14.7 14.7 0 0 1 0-4h4.6a14.7 14.7 0 0 1 0 4zm.3 5.6c.6-1.1 1.1-2.3 1.4-3.6h2.9a8 8 0 0 1-4.3 3.6zm1.7-5.6a16.5 16.5 0 0 0 0-4h3.4a8 8 0 0 1 0 4z"/></svg>
          <span>www.<span class="contact__accent">leafspire</span>.ch</span>
        </li>
      </ul>
    </div>
  </section>

  <section class="card card--back" aria-label="Business card back">
    <div class="wordmark">LeafSpire</div>
  </section>
</main>
</body>
</html>
```